Business Card Design Project

parking lot sealing and striping company

Industry/Entity Type

Business

Contact Information for Business Card

See pics below, blue and gray colors

```html
<!DOCTYPE html>
<html lang="en">
<head>
<meta charset="utf-8">
<title>Crestline Sealing – Business Card</title>
<link rel="stylesheet" href="https://fonts.googleapis.com/css2?family=Arimo:wght@400;700&display=swap">
<style>
  :root {
    --bg: #e8e9eb;
    --slate: #2f353c;
    --slate-deep: #23282e;
    --paper: #ffffff;
    --blue: #1f78c8;
    --gray-mid: #8a939c;
    --text-light: #eef1f4;
    --text-dark: #2a2f35;
  }
  * { box-sizing: border-box; margin: 0; padding: 0; }
  html, body { width: 1200px; height: 913px; overflow: hidden; }
  body {
    background: var(--bg);
    font-family: "Arimo", Arial, sans-serif;
    display: flex;
    align-items: center;
    justify-content: center;
    gap: 40px;
  }
  .card {
    position: relative;
    width: 520px;
    height: 297px;
    border-radius: 16px;
    overflow: hidden;
    box-shadow: 0 6px 18px rgba(0,0,0,0.18);
  }

  /* brand lockup */
  .brand { display: flex; align-items: center; gap: 12px; }
  .brand-mark { width: 52px; height: 52px; background: var(--blue); flex: none; }
  .brand-text { display: flex; flex-direction: column; gap: 6px; }
  .brand-name {
    color: var(--blue);
    font-weight: 700;
    font-size: 32px;
    letter-spacing: 1px;
    text-transform: uppercase;
    line-height: 1;
    white-space: nowrap;
  }
  .tagline {
    background: var(--blue);
    color: var(--paper);
    font-size: 12px;
    letter-spacing: 1.2px;
    text-transform: uppercase;
    padding: 3px 8px;
    white-space: nowrap;
  }

  /* front */
  .card-front { background: linear-gradient(160deg, var(--slate), var(--slate-deep)); }
  .card-front .brand { position: absolute; left: 56px; top: 72px; }
  .services {
    position: absolute;
    left: 38px; right: 28px; bottom: 46px;
    display: flex;
    justify-content: space-between;
  }
  .service-group { list-style: none; }
  .service-group li {
    color: var(--text-light);
    font-size: 13px;
    line-height: 1.5;
    display: flex;
    align-items: center;
    gap: 6px;
    white-space: nowrap;
  }
  .tick { width: 10px; height: 10px; flex: none; color: var(--blue); }

  /* back */
  .card-back { background: var(--paper); }
  .swoosh { position: absolute; inset: 0; width: 100%; height: 100%; }
  .swoosh-accent { fill: var(--blue); }
  .swoosh-body { fill: var(--slate); }
  .card-back .brand { position: absolute; right: 36px; top: 42px; gap: 9px; }
  .card-back .brand-mark { width: 38px; height: 38px; }
  .card-back .brand-name { font-size: 23px; }
  .card-back .tagline { font-size: 9px; padding: 2px 6px; }
  .contact { position: absolute; left: 34px; top: 170px; }
  .person-name {
    color: var(--blue);
    font-size: 19px;
    letter-spacing: 0.5px;
    text-transform: uppercase;
  }
  .name-rule { width: 34px; height: 2px; background: var(--gray-mid); margin: 8px 0 10px; }
  .contact-list { list-style: none; }
  .contact-list li {
    display: flex; align-items: center; gap: 8px;
    color: var(--text-dark);
    font-size: 12px;
    line-height: 1.55;
  }
  .contact-list .phone { font-size: 17px; }
  .icon { width: 10px; height: 10px; flex: none; color: var(--blue); }
</style>
</head>
<body>

<section class="card card-front" aria-label="Card front">
  <div class="brand">
    <div class="brand-mark"></div>
    <div class="brand-text">
      <span class="brand-name">Crestline Sealing</span>
      <span class="tagline">Smooth lots, lasting results</span>
    </div>
  </div>

  <div class="services">
    <ul class="service-group">
      <li><svg class="tick" viewBox="0 0 10 10"><path d="M1 5 L4 8 L9 1" fill="none" stroke="currentColor" stroke-width="2"/></svg>Asphalt Sealing</li>
      <li><svg class="tick" viewBox="0 0 10 10"><path d="M1 5 L4 8 L9 1" fill="none" stroke="currentColor" stroke-width="2"/></svg>Crack Repair</li>
      <li><svg class="tick" viewBox="0 0 10 10"><path d="M1 5 L4 8 L9 1" fill="none" stroke="currentColor" stroke-width="2"/></svg>Ramp Building</li>
    </ul>
    <ul class="service-group">
      <li><svg class="tick" viewBox="0 0 10 10"><path d="M1 5 L4 8 L9 1" fill="none" stroke="currentColor" stroke-width="2"/></svg>Line Painting</li>
      <li><svg class="tick" viewBox="0 0 10 10"><path d="M1 5 L4 8 L9 1" fill="none" stroke="currentColor" stroke-width="2"/></svg>Concrete Curb</li>
      <li><svg class="tick" viewBox="0 0 10 10"><path d="M1 5 L4 8 L9 1" fill="none" stroke="currentColor" stroke-width="2"/></svg>Walkway Sealing</li>
    </ul>
    <ul class="service-group">
      <li><svg class="tick" viewBox="0 0 10 10"><path d="M1 5 L4 8 L9 1" fill="none" stroke="currentColor" stroke-width="2"/></svg>Oil Stain Removal</li>
      <li><svg class="tick" viewBox="0 0 10 10"><path d="M1 5 L4 8 L9 1" fill="none" stroke="currentColor" stroke-width="2"/></svg>Parking Lot Clean Up</li>
      <li><svg class="tick" viewBox="0 0 10 10"><path d="M1 5 L4 8 L9 1" fill="none" stroke="currentColor" stroke-width="2"/></svg>Pothole And Gap Filling</li>
    </ul>
  </div>
</section>

<section class="card card-back" aria-label="Card back">
  <svg class="swoosh" viewBox="0 0 520 297" preserveAspectRatio="none" aria-hidden="true">
    <path class="swoosh-accent" d="M520 70 C 470 150 380 260 190 297 L 520 297 Z"/>
    <path class="swoosh-body" d="M520 62 C 478 150 400 255 215 297 L 520 297 Z"/>
    <rect class="swoosh-accent" x="0" y="291" width="520" height="6"/>
  </svg>

  <div class="brand">
    <div class="brand-mark"></div>
    <div class="brand-text">
      <span class="brand-name">Crestline Sealing</span>
      <span class="tagline">Smooth lots, lasting results</span>
    </div>
  </div>

  <div class="contact">
    <p class="person-name">Dale Morrison</p>
    <div class="name-rule"></div>
    <ul class="contact-list">
      <li class="phone"><svg class="icon" viewBox="0 0 10 10"><path d="M2 1 L4 1 L4.5 3 L3.3 3.8 Q4.3 5.8 6.2 6.7 L7 5.5 L9 6 L9 8 Q5 9 2.2 5.6 Q0.8 3.5 2 1 Z" fill="currentColor"/></svg>555.204.0187</li>
      <li><svg class="icon" viewBox="0 0 10 10"><rect x="0.5" y="2" width="9" height="6" fill="none" stroke="currentColor"/><path d="M0.5 2 L5 5.5 L9.5 2" fill="none" stroke="currentColor"/></svg>crestlinesealing@mail.com</li>
      <li><svg class="icon" viewBox="0 0 10 10"><circle cx="5" cy="5" r="4.3" fill="none" stroke="currentColor"/><ellipse cx="5" cy="5" rx="2" ry="4.3" fill="none" stroke="currentColor"/><path d="M0.7 5 H9.3" stroke="currentColor"/></svg>www.crestlinesealing.com</li>
    </ul>
  </div>
</section>

</body>
</html>
```